A5 Personal trainer profile for corbell vitality

I need a A5 Landscape profile designed for the company I work for. Company name is Corbell Vitality. The profile is for personal trainers to let people know:

1. Brief description of themselves
2. Qualifications

A picture will be required on the right hand side of the profile. Corbell Vitality colours are green and white.

The Corbell Vitality Logo in the boarder of the example included must remain. We are looking for a clinical and professional design.

Industry/Entity Type

Health

```html
<!DOCTYPE html>
<html lang="en">
<head>
<meta charset="utf-8">
<title>Personal Trainer Profile – Corbell Vitality</title>
<link rel="stylesheet" href="https://fonts.googleapis.com/css2?family=Arimo:wght@400;700&display=swap">
<style>
  :root {
    --stage: #e4e7e2;
    --card: #ffffff;
    --panel: #eef4cf;
    --panel-edge: #bccf93;
    --green-deep: #2b7a36;
    --green-band: #2f7d33;
    --green-light: #7cbc3d;
    --green-pale: #a9db5e;
    --ink: #1f2a1f;
    --white: #ffffff;
  }
  * { margin: 0; padding: 0; box-sizing: border-box; }
  html, body {
    width: 1200px; height: 991px; overflow: hidden;
    background: var(--stage);
    font-family: "Arimo", Arial, sans-serif;
  }
  .profile-card {
    position: absolute; left: 30px; top: 98px;
    width: 1140px; height: 794px;
    background: var(--card);
  }
  .profile-panel {
    position: absolute; left: 16px; top: 17px;
    width: 1105px; height: 707px;
    background: var(--panel);
    border: 1.5px solid var(--panel-edge);
    overflow: hidden;
  }
  .trainer-photo {
    position: absolute; left: 668px; top: 8px;
    width: 437px; height: 370px;
    background: radial-gradient(ellipse at 55% 45%, #6b4a36 0%, #5d4432 28%, #8fd25a 52%, rgba(143,210,90,0.55) 72%, rgba(238,244,207,0) 100%);
  }
  .training-photo {
    position: absolute; left: 647px; top: 414px;
    width: 441px; height: 293px;
    background: radial-gradient(ellipse at 50% 60%, rgba(120,150,90,0.55) 0%, rgba(160,185,120,0.35) 45%, rgba(238,244,207,0) 78%);
  }
  .role-title {
    position: absolute; left: 46px; top: 22px;
    font-size: 48px; letter-spacing: 9px;
    color: var(--green-deep); font-weight: 400;
  }
  .trainer-name {
    position: absolute; left: 38px; top: 68px;
    font-size: 106px; line-height: 1; letter-spacing: -1px;
    color: var(--green-deep); font-weight: 400;
  }
  .section-heading {
    position: absolute; left: 39px;
    font-size: 46px; font-weight: 400;
    color: var(--green-light);
  }
  .heading-help { top: 178px; }
  .heading-quals { top: 541px; }
  .bullet-list {
    position: absolute; left: 40px;
    list-style: none;
    font-size: 21.5px; line-height: 23px;
    color: var(--ink);
  }
  .bullet-list li::before { content: "• "; }
  .list-help { top: 237px; }
  .list-quals { top: 598px; }
  .testimonial-band {
    position: absolute; left: 19px; top: 369px;
    width: 1070px; height: 158px;
    background: var(--green-band);
    border-radius: 3px;
    opacity: 0.96;
  }
  .testimonial-band h2 {
    position: absolute; left: 20px; top: 8px;
    font-size: 46px; font-weight: 400;
    color: var(--green-pale);
  }
  .testimonial-band blockquote {
    position: absolute; left: 20px; top: 66px;
    width: 860px;
    font-size: 21.5px; line-height: 23px;
    color: var(--white);
  }
  .contact-line {
    position: absolute; left: 54px; top: 738px;
    font-size: 49px; color: var(--green-deep);
  }
  .brand-mark {
    position: absolute; right: 20px; top: 746px;
    display: flex; align-items: center; gap: 8px;
    font-size: 38px; font-weight: 700;
    color: var(--green-deep);
  }
  .brand-mark .brand-square {
    width: 30px; height: 30px;
    background: var(--green-deep);
  }
</style>
</head>
<body>
  <article class="profile-card">
    <section class="profile-panel">
      <div class="trainer-photo" role="img" aria-label="Portrait photo of the personal trainer smiling, wearing a green polo shirt"></div>
      <div class="training-photo" role="img" aria-label="Faded photo of a trainer coaching a client with a medicine ball"></div>

      <p class="role-title">Personal Trainer</p>
      <h1 class="trainer-name">MARCUS ODUYA</h1>

      <h2 class="section-heading heading-help">How I can help you?</h2>
      <ul class="bullet-list list-help">
        <li>Reduce body fat&nbsp; and increase body definition</li>
        <li>Increase stamina, improve agility and speed</li>
        <li>Increase strength and size</li>
        <li>Plyometric training and conditioning</li>
        <li>Flexibility and core strength</li>
      </ul>

      <div class="testimonial-band">
        <h2>What my clients say about me?</h2>
        <blockquote>"With Marcus my training is always challenging and fun. I don’t remember a session to be boring or repetitive. In short time I improved my core strength and flexibility. I can run 10k without stopping. It is amazing improvement.&nbsp; " Hannah Pellow</blockquote>
      </div>

      <h2 class="section-heading heading-quals">Qualifications</h2>
      <ul class="bullet-list list-quals">
        <li>Advanced Circuit Training</li>
        <li>Advanced Diploma in Personal Training - Level 3 FPR Registered</li>
        <li>Fitness Instructor - Level 2 FPR Registered</li>
        <li>Also qualified in – Suspension training, Studio Cycling, Sports Nutrition, Weight Management</li>
      </ul>
    </section>

    <p class="contact-line">Call Us Now 01632 960418</p>
    <div class="brand-mark"><span class="brand-square"></span>Corbell Vitality</div>
  </article>
</body>
</html>
```